Child Activity Courses Flyer with Free Post Slip

An A4 double sided flyer with a perforated tear off FREE POST slip at the bottom.

LOOK AT THE PDF EXAMPLE PROVIDED: Obviously, it shouldn’t look like this. But this has all the content in the rough layout we are after. We want it to look colourful, awesome, have pictures on it, and be generally attention-grabbing and attractive.

This flyer advertises our Child Activity and Healthy Eating Courses. These courses are given for free for children who are over a certain weight, for them and their parents to come once a week for 6 – 12 weeks, for a session learning about good healthy eating habits, physical activity, cooking healthy meals, etc.

The flyer should be colourful, attract attention, and in a visual way portray the positive benefits of the service; it should seem a fun, attractive course. It is aimed primarily at the parents as they will be the decision makers here, however it is being put into child’s bookbags (ages 5 – 12), so something that stands out to children - perhaps that they want to give their parents - is also good.

The main aim – and the design should support this – is for it to stand out, for parents to read the whole thing, and for it to look like an inviting slip that Parents want to send back to us. The purpose is to get as many returns - them tearing off the slip - as possible. The artwork should therefore have a clear visual segmentation that invites reading - a clear headline that leads onto the text body, and should be easy to read. (the text shouldn't be divided up all over the place, or at angles or anything else "stylistic" that actually makes it more difficult to read). The images should also have a clear purpose and not be there just for the sake of it (images could be whatever works best, might only be one single image...).

For this project we also need the original indesign or illustrator files as we will want to be able to edit some details for future editions.

Notice on the "smiley faces" for the question, these should go from UNHAPPY to HAPPY, or some other indication of "not useful" (1) up to "extremely useful" (2)

Target Market(s)

Parents of children aged 5 - 12 (all parents, but especially those whose children have high BMI or an above healthy weight)

Industry/Entity Type

Health And Wellness

Requirements
Must have
• All the wording shown in the PDF file attached. Also, probably in that layout as well. Unless there is a layout that you find works better to encourage everything to be read.
Should not have
• Anything that offends parents of overweight children

```html
<!DOCTYPE html>
<html lang="en">
<head>
<meta charset="utf-8">
<title>BrightStart Halton – Child Activity Course Flyer</title>
<link rel="stylesheet" href="https://fonts.googleapis.com/css2?family=Oswald:wght@500;700&family=Open+Sans:wght@400;600&family=Kalam:wght@700&display=swap">
<style>
  :root {
    --navy: #0f3f8c;
    --blue: #1f6fd1;
    --sky: #dce9f7;
    --orange: #f28a12;
    --orange-deep: #e0650a;
    --white: #ffffff;
    --ink: #1d3a6e;
    --page: #eef1f5;
  }
  * { box-sizing: border-box; margin: 0; padding: 0; }
  html, body { width: 900px; height: 1200px; overflow: hidden; background: var(--page); }
  .flyer {
    position: relative; width: 900px; height: 1200px; background: var(--white);
    font-family: "Open Sans", Arial, sans-serif; overflow: hidden;
  }
  .intro-panel {
    position: absolute; left: 28px; top: 28px; width: 520px; height: 400px;
    background: linear-gradient(160deg, var(--blue), var(--navy));
    border-radius: 0 0 60px 0;
  }
  .audience-tag {
    position: absolute; left: 28px; top: 28px; width: 470px; height: 52px;
    background: var(--orange); border-radius: 0 0 26px 0;
    color: var(--white); font-family: "Oswald", Arial, sans-serif; font-weight: 500;
    font-size: 21px; letter-spacing: .5px; line-height: 52px; padding-left: 26px;
  }
  .headline {
    position: absolute; left: 56px; top: 104px; width: 470px;
    font-family: "Oswald", Arial, sans-serif; font-weight: 700; text-transform: uppercase;
    font-size: 35px; line-height: 1.12; color: var(--orange);
  }
  .headline .light { color: var(--white); }
  .intro-copy {
    position: absolute; left: 56px; top: 300px; width: 460px;
    color: var(--white); font-size: 15px; line-height: 1.45; text-align: justify;
  }
  .family-photo {
    position: absolute; left: 568px; top: 30px; width: 320px; height: 320px; border-radius: 50%;
    background: radial-gradient(circle at 45% 40%, #f3d2bd, #c98c6a 55%, #8a5a44);
    border: 12px solid var(--blue); box-shadow: 0 0 0 5px var(--white), 0 0 0 9px var(--orange);
  }
  .swoosh { position: absolute; left: 0; top: 380px; width: 900px; height: 120px; }
  .child-photo {
    position: absolute; left: 0; top: 470px; width: 300px; height: 360px;
    background: linear-gradient(150deg, #f5cfb2, #d59a72 50%, #9c6a4c);
    border-radius: 0 40px 40px 0;
  }
  .offer-heading {
    position: absolute; left: 340px; top: 488px; width: 540px; height: 54px;
    border: 4px solid var(--blue); border-right: none; border-radius: 30px 0 0 30px;
    color: var(--orange-deep); font-family: "Oswald", Arial, sans-serif; font-weight: 700;
    font-size: 21px; line-height: 46px; text-align: center; text-transform: uppercase;
  }
  .offer-list {
    position: absolute; right: 34px; top: 570px; list-style: none; text-align: right;
    font-family: "Oswald", Arial, sans-serif; font-weight: 500; text-transform: uppercase;
    color: var(--ink); font-size: 22px; line-height: 1.75;
  }
  .offer-list li::after {
    content: ""; display: inline-block; width: 12px; height: 12px; border-radius: 50%;
    background: var(--blue); margin-left: 14px; vertical-align: middle;
  }
  .brand {
    position: absolute; left: 340px; top: 766px; width: 540px;
    display: flex; align-items: center; justify-content: center; gap: 10px;
    font-family: "Oswald", Arial, sans-serif; font-weight: 700; color: var(--orange-deep);
    font-size: 30px;
  }
  .brand-dot { width: 22px; height: 22px; border-radius: 50%; background: var(--blue); }
  .return-band {
    position: absolute; left: 0; top: 840px; width: 900px; height: 62px; background: var(--blue);
    color: var(--white); font-family: "Kalam", cursive; font-weight: 700; font-size: 23px;
    line-height: 62px; text-align: center;
  }
  .tear-line {
    position: absolute; left: 0; top: 930px; width: 900px; border-top: 3px dashed var(--navy);
  }
  .tear-note {
    position: absolute; left: 40px; top: 912px; font-size: 11px; color: var(--ink);
  }
  .slip {
    position: absolute; left: 0; top: 932px; width: 900px; height: 268px; background: var(--sky);
  }
  .slip-box {
    position: absolute; top: 28px; width: 120px; height: 60px; background: var(--white);
  }
  .slip-box.left { left: 60px; }
  .slip-box.right { right: 60px; }
  .address {
    position: absolute; left: 330px; top: 100px; width: 240px; padding: 16px 0;
    background: var(--white); border: 3px solid var(--navy); text-align: center;
    font-family: "Oswald", Arial, sans-serif; font-weight: 500; font-style: normal; color: var(--navy);
    font-size: 20px; line-height: 1.3;
  }
</style>
</head>
<body>
<main class="flyer">
  <section class="intro-panel"></section>
  <div class="audience-tag">FOR THE ATTENTION OF PARENTS / CARERS</div>
  <h1 class="headline">Fill in the form below <span class="light">for your chance to</span> change your family's <span class="light">lifestyle for the better</span></h1>
  <p class="intro-copy">It's difficult in this modern world full of sugary drinks, fast food, snacks and computer games to keep a good eye on your child's lifestyle and to avoid the health problems that can come from them being above a healthy weight.</p>

  <div class="family-photo" role="img" aria-label="Photo of a grandmother, parent and child cooking together in a kitchen"></div>

  <svg class="swoosh" viewBox="0 0 900 120" aria-hidden="true">
    <path d="M0 95 C250 40 600 40 900 20 L900 50 C600 70 250 75 0 120 Z" fill="var(--orange)"/>
    <path d="M0 80 C250 30 600 25 900 5 L900 18 C600 40 250 50 0 95 Z" fill="var(--blue)"/>
  </svg>

  <div class="child-photo" role="img" aria-label="Photo of a child biting into a sandwich"></div>

  <h2 class="offer-heading">Our activity course offers your child the chance to:</h2>
  <ul class="offer-list">
    <li>Learn how much sugar is in their drinks</li>
    <li>Find out what food labels actually mean</li>
    <li>Recipes that taste delicious</li>
    <li>Discover how to shop smart in a supermarket</li>
  </ul>

  <div class="brand"><span class="brand-dot"></span>BrightStart Halton</div>

  <p class="return-band">Fill in this form and send it back and we'll be in touch to give you more information</p>

  <p class="tear-note">Tear along this line and put in the post</p>
  <div class="tear-line"></div>

  <section class="slip">
    <div class="slip-box left"></div>
    <div class="slip-box right"></div>
    <address class="address">BRIGHTSTART HALTON<br>14 Meadow Road<br>HALTON<br>HT4 2QB</address>
  </section>
</main>
</body>
</html>
```